Northwind Crate Traders Needs a FRESH website

We would like a creative minded designer to take on the task to Re-design our website. Its a simple 5-7 pages. With no cart, no complex html. Just plain information about our company and products we import and export. Pictures added to the product section. Since Our logo its Blue, we would like the designer to use complementing colors in order to make the website look cleaner and modern.

Target Market(s)

The target audience will be companies looking to purchase plastic related products. Companies looking to purchase large quantities of plastic containers (Shampoo bottles, caps, sprayers, mist sprayers, cosmetic containers etc).

Industry/Entity Type

It Company

Font styles to use
Sans Serif

Requirements
Must have
• We have a section in which we would like to add pictures of some of the products we carry, therefore having an easy and clean way to navigate through the pictures will be a plus.

```html
<!DOCTYPE html>
<html lang="en">
<head>
<meta charset="utf-8">
<title>Northwind Crate Traders</title>
<link href="https://fonts.googleapis.com/css2?family=Open+Sans:wght@400;600;700&family=Noto+Serif:ital@1&display=swap" rel="stylesheet">
<style>
:root{
  --blue:#0a8fd6;
  --blue-dark:#0b5fa8;
  --navy:#0d4e9a;
  --bar:#5f5f5f;
  --bar-btn:#7a7a7a;
  --text:#555;
  --text-light:#777;
  --panel:#f2f2f2;
  --line:#d6d6d6;
  --footer:#595959;
  --white:#fff;
}
*{box-sizing:border-box;margin:0;padding:0}
html,body{width:993px;height:1200px;overflow:hidden;background:var(--white);font-family:"Open Sans",Arial,sans-serif;color:var(--text)}
.page{position:relative;width:993px;height:1200px}
.abs{position:absolute}

/* top bar */
.top-bar{left:0;top:0;width:993px;height:20px;background:var(--blue)}
.top-phone{right:172px;top:4px;font-size:8px;font-weight:700;color:var(--white)}
.top-login{left:882px;top:0;width:45px;height:20px;background:var(--blue-dark);color:var(--white);font-size:8px;display:flex;align-items:center;justify-content:center;gap:3px}

/* header */
.brand{left:100px;top:27px;display:flex;align-items:center;gap:8px}
.brand-dot{width:48px;height:48px;border-radius:50%;background:var(--blue)}
.brand-name{font-size:18px;font-weight:600;color:var(--blue);line-height:1.1;width:150px}
.nav{top:40px;left:502px;display:flex;align-items:center;font-size:9.5px;font-weight:600;color:var(--blue);text-transform:uppercase}
.nav a{color:inherit;text-decoration:none}
.nav-home{left:502px;width:47px;height:25px;background:var(--blue);color:var(--white)!important;display:flex;align-items:center;justify-content:center;border-radius:2px}
.nav-item{top:47px}

/* hero */
.hero{left:100px;top:80px;width:827px;height:371px;border:1px solid #bdbdbd;overflow:hidden;
  background:linear-gradient(90deg,#fbfbfb 0%,#f6eef0 28%,#e7e2da 40%,#9fd8e4 55%,#5f9fe0 68%,#7fd0d8 82%,#cfe8ee 100%)}
.hero-title{left:43px;top:91px;height:43px;padding:0 10px;background:rgba(85,85,85,.88);color:var(--white);font-size:26px;font-weight:400;display:flex;align-items:center}
.hero-sub{left:43px;top:148px;height:36px;padding:0 8px;background:rgba(85,85,85,.88);color:var(--white);font-size:15px;display:flex;align-items:center}
.hero-btn{left:43px;top:204px;width:87px;height:29px;background:var(--blue);color:var(--white);font-size:13px;border-radius:3px;display:flex;align-items:center;justify-content:center}
.hero-pager{left:290px;top:343px;width:246px;height:16px;background:#333;border-radius:4px;padding:4px 6px;display:flex;gap:3px}
.hero-pager span{flex:1;background:var(--white)}
.hero-pager span.on{background:var(--blue)}
.hero-corner{bottom:0;width:56px;height:56px}

/* section bars */
.bar{height:38px;background:var(--bar);color:var(--white);font-size:11px;font-weight:700;text-transform:uppercase;display:flex;align-items:center}
.bar-icon{width:45px;height:38px;background:var(--blue);display:flex;align-items:center;justify-content:center;position:relative;margin-right:17px}
.bar-icon::after{content:"";position:absolute;right:-7px;top:12px;border-left:7px solid var(--blue);border-top:7px solid transparent;border-bottom:7px solid transparent}
.bar-arrows{margin-left:auto;margin-right:7px;display:flex;gap:4px}
.bar-arrows span{width:23px;height:23px;background:var(--bar-btn);display:flex;align-items:center;justify-content:center}

/* product tiles */
.tile{top:517px;width:194px;height:128px;border:1px solid var(--line)}
.tile-feature{background:var(--blue);color:var(--white);padding:11px 15px;border-color:var(--blue)}
.tile-feature h3{font-size:12px;font-weight:700;line-height:1.35}
.tile-feature p{font-size:9px;line-height:1.55;margin-top:3px}
.tile-tools{right:0;bottom:0;display:flex;gap:2px}
.tile-tools span{width:26px;height:26px;background:var(--blue-dark);display:flex;align-items:center;justify-content:center}

/* callout */
.callout{left:100px;top:663px;width:827px;height:72px;background:var(--panel);border:1px solid #e4e4e4}
.callout-text{left:14px;top:25px;width:700px;white-space:nowrap;font-size:12px;color:#222}
.callout-text strong{font-size:16px;font-weight:700}
.callout-btn{left:721px;top:22px;width:96px;height:29px;background:var(--blue);color:var(--white);font-size:11px;border-radius:2px;display:flex;align-items:center;justify-content:center}

/* columns */
.welcome-text{left:100px;top:814px;width:263px;font-size:10.5px;line-height:22.6px;color:var(--text-light)}
.product-intro{left:381px;top:812px;white-space:nowrap;font-size:11.5px;line-height:22.6px;color:var(--text)}
.product-list{left:381px;top:862px;width:270px;list-style:none;font-size:11.5px;color:var(--text)}
.product-list li{display:flex;align-items:center;height:36.5px;gap:12px;white-space:nowrap}
.product-list svg{width:22px;height:22px;flex:none}
.testimonial{left:664px;top:806px;width:263px}
.quote{position:relative;background:var(--panel);border:1px solid var(--line);padding:11px 14px;font-family:"Noto Serif",Georgia,serif;font-style:italic;font-size:10px;line-height:18px;color:#555}
.quote::after{content:"";position:absolute;left:13px;bottom:-9px;border-top:9px solid var(--panel);border-right:9px solid transparent}
.quote-name{margin-top:11px;font-family:"Noto Serif",Georgia,serif;font-style:italic;color:var(--blue);font-size:12px;line-height:1.1}
.quote-name small{display:block;font-size:7.5px;font-weight:700}

/* footer */
.footer{left:0;top:1157px;width:993px;height:43px;background:var(--footer);color:var(--white);font-size:10.5px}
.footer-copy{left:100px;top:15px}
.footer-links{right:66px;top:15px}
</style>
</head>
<body>
<div class="page">

  <div class="abs top-bar"></div>
  <div class="abs top-phone">(00) 4321 8765 010</div>
  <div class="abs top-login">
    <svg width="7" height="8" viewBox="0 0 7 8"><rect x="0" y="3.5" width="7" height="4.5" fill="#fff"/><path d="M1.5 3.5V2.3a2 2 0 0 1 4 0v1.2" stroke="#fff" fill="none"/></svg>Login
  </div>

  <header>
    <div class="abs brand">
      <div class="brand-dot"></div>
      <div class="brand-name">Northwind Crate Traders</div>
    </div>
    <nav>
      <a class="abs nav-home" style="top:40px;font-size:9.5px;font-weight:600">HOME</a>
      <a class="abs nav nav-item" style="left:577px;top:47px">About us</a>
      <a class="abs nav nav-item" style="left:660px;top:47px">Products</a>
      <a class="abs nav nav-item" style="left:745px;top:47px">Mission statement</a>
      <a class="abs nav nav-item" style="left:872px;top:47px">Contact us</a>
    </nav>
  </header>

  <section class="abs hero" role="img" aria-label="Photo of pastel plastic shampoo and lotion bottles with pump and spray caps">
    <h1 class="abs hero-title">Northwind Crate Traders</h1>
    <div class="abs hero-sub">You Dream It And We Deliver It</div>
    <div class="abs hero-btn">Read More</div>
    <div class="abs hero-pager"><span></span><span class="on"></span><span></span><span></span></div>
    <svg class="abs hero-corner" style="left:0" viewBox="0 0 56 56"><path d="M0 0L56 56H0Z" fill="var(--navy)"/><path d="M16 28l-4 4 4 4" stroke="#fff" stroke-width="1.5" fill="none"/></svg>
    <svg class="abs hero-corner" style="right:0" viewBox="0 0 56 56"><path d="M56 0V56H0Z" fill="var(--navy)"/><path d="M40 28l4 4-4 4" stroke="#fff" stroke-width="1.5" fill="none"/></svg>
  </section>

  <div class="abs bar" style="left:100px;top:468px;width:827px">
    <div class="bar-icon"><svg width="18" height="14" viewBox="0 0 18 14"><rect x="1" y="1" width="16" height="12" fill="none" stroke="#fff" stroke-width="1.5"/><path d="M3 11l4-4 3 3 2-2 3 3" stroke="#fff" fill="none"/></svg></div>
    Our Products
    <div class="bar-arrows">
      <span><svg width="8" height="10"><path d="M6 1L2 5l4 4" stroke="#fff" fill="none"/></svg></span>
      <span><svg width="8" height="10"><path d="M2 1l4 4-4 4" stroke="#fff" fill="none"/></svg></span>
    </div>
  </div>

  <div class="abs tile" style="left:100px;background:linear-gradient(135deg,#fff 10%,#9a9ea3 40%,#6e7378 60%,#fff 90%)" role="img" aria-label="Steel injection mould block"></div>
  <div class="abs tile tile-feature" style="left:311px">
    <h3>Proin gravida nibh vel velit auctor</h3>
    <p>Lorem quis bibendum auctor, nisi elit consequat ipsum, nec sagittis sem nibh id elit. Duis sed odio sit</p>
    <div class="abs tile-tools">
      <span><svg width="14" height="14"><circle cx="6" cy="6" r="4" stroke="#fff" fill="none" stroke-width="1.5"/><path d="M9 9l4 4" stroke="#fff" stroke-width="1.8"/></svg></span>
      <span><svg width="14" height="14"><rect x="1" y="4" width="9" height="9" stroke="#fff" fill="none" stroke-width="1.5"/><path d="M6 8l7-7M9 1h4v4" stroke="#fff" fill="none" stroke-width="1.5"/></svg></span>
    </div>
  </div>
  <div class="abs tile" style="left:522px;background:radial-gradient(circle at 55% 55%,#f2d23a 0 22%,#f5f5f5 38%,#fff 70%)" role="img" aria-label="White and yellow trigger spray head"></div>
  <div class="abs tile" style="left:733px;background:linear-gradient(90deg,#3b3f44,#8fa8bb 30%,#3f8fc9 50%,#1e2a33 70%,#4c9dd6 88%,#5a6066)" role="img" aria-label="Row of clear, blue and black plastic vials"></div>

  <section class="abs callout">
    <p class="abs callout-text"><strong>Northwind Crate</strong> is A trustworthy company sourcing and importing your needs to your business doorsteps.</p>
    <div class="abs callout-btn">Contact Us Now</div>
  </section>

  <div class="abs bar" style="left:100px;top:757px;width:263px">
    <div class="bar-icon"><svg width="18" height="16" viewBox="0 0 18 16"><path d="M1 1h16v10H7l-4 4v-4H1z" fill="none" stroke="#fff" stroke-width="1.5"/><path d="M5 5h8M5 8h6" stroke="#fff"/></svg></div>
    Welcome to Northwind Crate
  </div>
  <div class="abs bar" style="left:381px;top:757px;width:264px">
    <div class="bar-icon"><svg width="18" height="16" viewBox="0 0 18 16"><rect x="1" y="2" width="16" height="13" fill="none" stroke="#fff" stroke-width="1.5"/><circle cx="9" cy="7" r="2.3" fill="#fff"/><path d="M5 13c1-3 7-3 8 0" fill="#fff"/></svg></div>
    Our Products
  </div>
  <div class="abs bar" style="left:664px;top:757px;width:263px">
    <div class="bar-icon"><svg width="18" height="18" viewBox="0 0 18 18"><circle cx="8" cy="5" r="3.5" fill="#fff"/><path d="M2 17c0-5 3-7 6-7s4 1 5 2" fill="#fff"/><path d="M10 14l2 2 5-5" stroke="#fff" stroke-width="1.8" fill="none"/></svg></div>
    Client Testimonials
    <div class="bar-arrows">
      <span><svg width="8" height="10"><path d="M6 1L2 5l4 4" stroke="#fff" fill="none"/></svg></span>
      <span><svg width="8" height="10"><path d="M2 1l4 4-4 4" stroke="#fff" fill="none"/></svg></span>
    </div>
  </div>

  <div class="abs welcome-text">
    <p>Northwind Crate Traders will be your first and last stop for sourcing products from all over the world, specifically Asia and South America.</p>
    <p>We have partners all around the globe that helps us make the best decision in sourcing a product from and to any market.</p>
    <p>Northwind Crate Traders will always make the right choice for our clients when dealing with factories all over the world.</p>
    <p>We at Northwind Crate Traders have a great relationship with our suppliers which leads us to become more efficient at sourcing products and delivering it to our clients.</p>
  </div>

  <p class="abs product-intro">Not only in the plastic industry, but here are<br>some of the products we are currently sourcing</p>
  <ul class="abs product-list">
    <li><svg viewBox="0 0 22 22"><path d="M11 5a5 5 0 0 0-3 9v3h6v-3a5 5 0 0 0-3-9z" fill="#555"/><rect x="8.5" y="18" width="5" height="2" fill="#555"/><path d="M11 1v2M3 5l1.5 1.5M19 5l-1.5 1.5M1 11h2M19 11h2" stroke="#555"/></svg>Lights and lighting, LED, flashlights etc.</li>
    <li><svg viewBox="0 0 22 22"><rect x="5" y="2" width="12" height="18" fill="#555"/><rect x="7" y="4" width="6" height="14" fill="#fff"/><circle cx="14.5" cy="11" r="1" fill="#fff"/></svg>Doors: wood, steel</li>
    <li><svg viewBox="0 0 22 22"><rect x="3" y="3" width="16" height="16" fill="none" stroke="#555" stroke-width="2"/><path d="M3 11h16M9 7h4M9 15h4" stroke="#555" stroke-width="2"/></svg>Kitchen and bathroom cabinets</li>
    <li><svg viewBox="0 0 22 22"><path d="M10 3h2v5h-2zM3 8h16v3H3zM10 11h2v6h-2z" fill="#555"/><path d="M8 19h6" stroke="#555" stroke-width="2"/></svg>Plumbing products / bathroom products</li>
    <li><svg viewBox="0 0 22 22"><circle cx="11" cy="5" r="3" fill="#555"/><path d="M5 20v-8a6 6 0 0 1 12 0v8z" fill="#555"/></svg>Clothing: t-shirts, aprons, jute bags, caps,</li>
    <li><svg viewBox="0 0 22 22"><rect x="3" y="7" width="16" height="12" rx="2" fill="#555"/><rect x="6" y="10" width="8" height="6" fill="#fff"/><path d="M8 2l3 5 3-5" stroke="#555" fill="none" stroke-width="1.5"/></svg>Electronic: home, personal</li>
    <li><svg viewBox="0 0 22 22"><rect x="6" y="4" width="10" height="14" fill="#555"/><path d="M3 7h3M3 11h3M3 15h3M16 7h3M16 11h3M16 15h3" stroke="#555" stroke-width="1.5"/></svg>Integrated circuits and electronics</li>
  </ul>

  <div class="abs testimonial">
    <blockquote class="quote">Aenean sollicitudin, lorem quis bibendum auctor, nisi elit consequat ipsum, nec sagittis sem nibh id elit. Duis sed odio sit amet nibh vulputate cursus a sit amet mauris. Morbi accumsan ipsum velit. Nam nec tellus a odio tincidunt auctor a ornare odio. Sed non mauris vitae erat consequat auctor eu in elit.</blockquote>
    <div class="quote-name">Daniel Reyes<small>C.E.O Company</small></div>
  </div>

  <footer class="abs footer">
    <div class="abs footer-copy">Copyright © 2014 Northwind Crate Traders LLC, unless otherwise noted</div>
    <div class="abs footer-links">site map &nbsp;|&nbsp; privacy policy &nbsp;|&nbsp; disclaimer</div>
  </footer>
</div>
</body>
</html>
```